Blue Heron IT Business Card - Clean, Simple

Need a simple, clean standard sized business card for an IT consulting business using existing logo and company colours. Background should be mainly white. Feel free to be creative but clean, simple, quiet design is preferred. Font is specified in logo but any sans serif fonts work.

Contact Information for card is as follows (doesn't need to be in this exact order):

Malcolm Pettigrew
Owner
malcolm@blueheronit.ca
705-412-9083
www.blueheronit.ca

Target Market(s)

Small to medium sized business.

Industry/Entity Type

IT Consulting

Contact Information for Business Card

Logo and contact info.

Font styles to use
Sans Serif

Colors
EE7325
F08F49
F5BC92
FAE3D3
FDF4ED

Requirements
Must have
• All white or mostly white background.

```html
<!DOCTYPE html>
<html lang="en">
<head>
<meta charset="utf-8">
<title>Blue Heron IT Business Card</title>
<link rel="stylesheet" href="https://fonts.googleapis.com/css2?family=Montserrat:wght@400;500;700&display=swap">
<style>
  :root {
    --orange: #EE7325;
    --orange-soft: #F08F49;
    --ink: #2a2a2a;
    --rule: #9a9a9a;
    --paper: #ffffff;
    --night: #17181a;
    --night-mid: #1e1f22;
    --backdrop: #e9e7e4;
  }
  * { margin: 0; padding: 0; box-sizing: border-box; }
  html, body {
    width: 1200px; height: 1108px; overflow: hidden;
    background: var(--backdrop);
    font-family: "Montserrat", sans-serif;
  }
  .canvas {
    position: relative; width: 1200px; height: 1108px;
    display: flex; justify-content: center; align-items: center; gap: 80px;
  }
  .card {
    width: 390px; height: 682px; border-radius: 26px;
    position: relative; overflow: hidden;
    box-shadow: 0 10px 30px rgba(0,0,0,0.12);
  }
  .card-front {
    background: var(--paper);
    display: flex; flex-direction: column; align-items: center;
  }
  .brand {
    margin-top: 170px;
    display: flex; align-items: center; gap: 14px;
  }
  .brand-dot {
    width: 22px; height: 22px; border-radius: 50%; background: var(--orange);
  }
  .brand-name {
    font-weight: 500; font-size: 42px; color: var(--ink); letter-spacing: -0.5px;
  }
  .person { margin-top: 230px; text-align: center; }
  .person-name { font-weight: 700; font-size: 24px; color: var(--ink); letter-spacing: 0.5px; }
  .person-role { font-weight: 400; font-size: 19px; color: var(--orange); margin-top: 2px; }
  .icon-rule {
    display: flex; align-items: center; gap: 8px; margin-top: 14px; width: 300px;
  }
  .icon-rule .line { flex: 1; height: 1px; background: var(--rule); }
  .icon-box {
    width: 30px; height: 30px; border-radius: 6px; background: var(--orange);
    display: flex; align-items: center; justify-content: center;
  }
  .contact { margin-top: 14px; text-align: center; color: var(--ink); font-size: 19px; line-height: 1.35; font-weight: 500; }
  .contact .accent { color: var(--orange); }
  .card-back { background: var(--night); }
  .back-pattern {
    position: absolute; inset: 0;
    background: linear-gradient(225deg, #5a5b5e 0%, #2c2d30 40%, var(--night) 75%);
  }
</style>
</head>
<body>
<main class="canvas">
  <section class="card card-front">
    <div class="brand">
      <span class="brand-dot"></span>
      <span class="brand-name">Blue Heron IT</span>
    </div>
    <div class="person">
      <p class="person-name">Malcolm Pettigrew</p>
      <p class="person-role">Owner</p>
    </div>
    <div class="icon-rule">
      <span class="line"></span>
      <span class="icon-box">
        <svg width="18" height="18" viewBox="0 0 24 24" fill="#fff"><path d="M6.6 10.8a15 15 0 0 0 6.6 6.6l2.2-2.2c.3-.3.7-.4 1-.2 1.1.4 2.3.6 3.6.6.6 0 1 .4 1 1V20c0 .6-.4 1-1 1A17 17 0 0 1 3 4c0-.6.4-1 1-1h3.5c.6 0 1 .4 1 1 0 1.3.2 2.5.6 3.6.1.3 0 .7-.2 1z"/></svg>
      </span>
      <span class="icon-box">
        <svg width="18" height="18" viewBox="0 0 24 24" fill="none" stroke="#fff" stroke-width="2"><rect x="3" y="6" width="18" height="12" rx="1"/><path d="M3 7l9 6 9-6"/></svg>
      </span>
      <span class="icon-box">
        <svg width="18" height="18" viewBox="0 0 24 24" fill="none" stroke="#fff" stroke-width="2"><circle cx="12" cy="12" r="9"/><path d="M3 12h18M12 3c3 3 3 15 0 18M12 3c-3 3-3 15 0 18"/></svg>
      </span>
      <span class="line"></span>
    </div>
    <div class="contact">
      <p>705-412-9083</p>
      <p>malcolm@blueheronit.ca</p>
      <p>www.<span class="accent">blueheronit</span>.ca</p>
    </div>
  </section>

  <section class="card card-back">
    <div class="back-pattern" role="img" aria-label="Repeating pattern of the brand symbol in glossy black and grey tones, with a single orange symbol near the lower right"></div>
  </section>
</main>
</body>
</html>
```